Flyer Rework for Accountants and Lawyers

Information flyer for accountants and lawyers. Text and flowchart provided. Just need to make it look presentable for print and email. Needs to add logo (AI file provided) and provide graphics. No more than two pages. Our corporate visual identify guidelines are attached (MUST Use). Completed on both AI file and PPTX file.
Target Market(s)
Accountants, Company Directors and Lawyers
Industry/Entity Type
Finance And Accounting
Requirements
Must have
- Our corporate visual identify guidelines are attached (MUST Use)

```html
<!DOCTYPE html>
<html lang="en">
<head>
<meta charset="utf-8">
<title>Northfield Advisory – Director Penalty Notices Flyer</title>
<link href="https://fonts.googleapis.com/css2?family=Oswald:wght@500;700&family=Open+Sans:wght@400;600;700&display=swap" rel="stylesheet">
<style>
  :root{
    --green:#5db33b;
    --dark:#2b2b2b;
    --ink:#1a1a1a;
    --grey:#7a7a7a;
    --light:#f2f3f4;
    --stage:#dcdcdc;
    --white:#ffffff;
  }
  *{box-sizing:border-box;margin:0;padding:0}
  html,body{width:1200px;height:900px;overflow:hidden}
  body{background:var(--stage);font-family:"Open Sans",Arial,sans-serif;color:var(--ink);position:relative}
  .page{position:absolute;left:290px;width:620px;height:438px;background:var(--white);overflow:hidden;box-shadow:0 4px 14px rgba(0,0,0,.18)}
  .page--front{top:8px}
  .page--back{top:454px}
  .page__art{position:absolute;inset:0;width:620px;height:438px}
  .abs{position:absolute}

  /* front */
  .brand{left:26px;top:24px;display:flex;align-items:center;gap:10px}
  .brand__dot{width:44px;height:44px;border-radius:50%;border:5px solid var(--green)}
  .brand__name{font-weight:700;font-size:15px;color:var(--green);letter-spacing:.5px}
  .brand__tag{font-size:8px;color:var(--grey);margin-top:1px}
  .headline{left:40px;top:150px;font-family:"Oswald",Arial,sans-serif;font-weight:700;line-height:.95}
  .headline__small{font-size:20px;color:var(--ink)}
  .headline__mid{font-size:50px;color:var(--ink);letter-spacing:-.5px}
  .headline__big{font-size:62px;color:var(--green);letter-spacing:-.5px}
  .front-intro{left:42px;top:302px;width:250px;font-size:9.5px;line-height:1.4;text-align:justify}
  .help{right:22px;top:302px;text-align:right;font-family:"Oswald",Arial,sans-serif;font-weight:700;font-size:15px;color:var(--green);line-height:1.1}
  .help-text{right:22px;top:348px;width:250px;font-size:7.5px;line-height:1.4;text-align:justify}
  .web{font-size:8px;color:var(--white);letter-spacing:3px;font-weight:600}
  .front-web{right:120px;bottom:3px}

  /* back */
  .section-bar{left:0;top:12px;width:345px;height:22px;background:var(--green);color:var(--white);font-family:"Oswald",Arial,sans-serif;font-weight:700;font-size:12px;padding:3px 0 0 130px}
  .back-intro{left:24px;top:40px;width:390px;font-size:7.5px;line-height:1.35}
  .back-lead{left:24px;top:72px;width:390px;font-size:7.5px;font-weight:700;line-height:1.35}
  .facts{left:24px;top:100px;width:390px;border:1px solid #cfcfcf;background:var(--white)}
  .facts__head{height:16px;background:var(--dark);color:var(--white);font-family:"Oswald",Arial,sans-serif;font-weight:500;font-size:8.5px;padding:2px 0 0 130px;letter-spacing:.4px}
  .facts__row{display:flex;height:34px}
  .facts__row--tall{height:44px}
  .facts__label{width:112px;background:var(--green);color:var(--white);font-weight:700;font-size:6.5px;display:flex;align-items:center;justify-content:center;text-align:center;line-height:1.2;padding:0 14px 0 5px;position:relative}
  .facts__label::after{content:"";position:absolute;right:-7px;top:50%;width:14px;height:14px;margin-top:-7px;border-radius:50%;background:var(--white);border:2px solid var(--green)}
  .facts__label::before{content:"";position:absolute;right:-3px;top:50%;margin-top:-3px;border-left:5px solid var(--dark);border-top:3px solid transparent;border-bottom:3px solid transparent;z-index:1}
  .facts__text{flex:1;font-size:6.5px;line-height:1.3;padding:4px 6px 0 14px}
  .facts__options{display:flex;gap:6px;margin-top:3px}
  .facts__options span{flex:1;border-left:1px solid #bbb;padding-left:4px}
  .facts__options span:first-child{border:0;padding:0}
  .tips-bar{left:24px;top:304px;width:390px;height:18px;background:var(--dark);color:var(--white);font-family:"Oswald",Arial,sans-serif;font-weight:700;font-size:10px;padding:2px 0 0 60px}
  .tips{left:24px;top:328px;width:390px;display:flex;gap:16px;font-size:7px;line-height:1.35;text-align:justify}
  .tips p{flex:1}
  .tips p + p{flex:1.15}
  .tips .gap{margin-top:5px;display:block}
  .node{position:absolute;display:flex;align-items:center;justify-content:center;text-align:center;font-size:6px;line-height:1.2;color:var(--ink)}
  .node--bold{font-weight:700}
  .tagpill{position:absolute;background:var(--dark);color:var(--white);font-size:6px;border-radius:8px;padding:1px 5px}
  .flow-note{position:absolute;font-size:6.3px;line-height:1.3;text-align:center}
  .back-web{left:250px;bottom:3px}
</style>
</head>
<body>

<section class="page page--front">
  <svg class="page__art" viewBox="0 0 620 438">
    <defs>
      <linearGradient id="photoTone" x1="0" y1="0" x2="1" y2="0.4">
        <stop offset="0" stop-color="#ffffff"/>
        <stop offset=".45" stop-color="#e9ecef"/>
        <stop offset=".75" stop-color="#8a93a0"/>
        <stop offset="1" stop-color="#3b4350"/>
      </linearGradient>
      <linearGradient id="lowerTone" x1="0" y1="0" x2="0" y2="1">
        <stop offset="0" stop-color="#eceeef"/>
        <stop offset="1" stop-color="#ffffff"/>
      </linearGradient>
    </defs>
    <polygon points="395,264 452,296 620,170 620,438 330,438" fill="url(#lowerTone)"/>
    <polygon points="0,0 620,0 620,165 452,292 398,262 0,28" fill="url(#photoTone)" role="img" aria-label="Photo of two businessmen reviewing documents on a tablet at a desk"/>
    <polyline points="392,266 452,300 620,172" fill="none" stroke="var(--green)" stroke-width="4"/>
    <polygon points="300,438 318,422 620,422 620,438" fill="var(--dark)"/>
  </svg>

  <div class="abs brand">
    <span class="brand__dot"></span>
    <div>
      <div class="brand__name">NORTHFIELD ADVISORY</div>
      <div class="brand__tag">Restructuring &amp; Solvency Accountants</div>
    </div>
  </div>

  <h1 class="abs headline">
    <div class="headline__small">INDEPENDENT</div>
    <div class="headline__mid">CONCISE</div>
    <div class="headline__big">EFFICIENT</div>
  </h1>

  <p class="abs front-intro">Company directors and their advisors need to be aware that non-lodgement of Business Activities Statements (“BAS”) and Superannuation Guarantee Charge (“SCG”) Statements with the ATO may be personally liability for these debts.</p>

  <h2 class="abs help">How Northfield Advisory<br>can help?</h2>
  <p class="abs help-text">Company directors and their advisors need to be aware that non-lodgement of Business Activities Statements (“BAS”) and Superannuation Guarantee Charge (“SCG”) Statements with the ATO may be personally liability for these debts.</p>

  <div class="abs web front-web">www.northfieldadvisory.com.au</div>
</section>

<section class="page page--back">
  <svg class="page__art" viewBox="0 0 620 438">
    <rect x="420" y="0" width="200" height="438" fill="var(--light)" opacity=".6"/>
    <g fill="none" stroke-width="3">
      <circle cx="492" cy="62" r="40" stroke="#d6d6d6"/>
      <circle cx="492" cy="62" r="40" stroke="var(--green)" stroke-dasharray="150 252" transform="rotate(10 492 62)"/>
      <circle cx="572" cy="150" r="34" stroke="#d6d6d6"/>
      <circle cx="572" cy="150" r="34" stroke="var(--green)" stroke-dasharray="120 214" transform="rotate(10 572 150)"/>
      <circle cx="470" cy="182" r="34" stroke="#d6d6d6"/>
      <circle cx="470" cy="182" r="34" stroke="var(--green)" stroke-dasharray="120 214" transform="rotate(10 470 182)"/>
    </g>
    <g fill="none" stroke-width="1.5">
      <polyline points="492,102 492,116" stroke="var(--dark)"/>
      <polyline points="450,124 450,116 568,116 568,112" stroke="var(--green)"/>
      <polygon points="446,124 454,124 450,130" fill="var(--green)" stroke="none"/>
      <polygon points="564,112 572,112 568,118" fill="var(--green)" stroke="none" transform="rotate(180 568 115)"/>
      <line x1="505" y1="172" x2="530" y2="164" stroke="var(--dark)"/>
      <polyline points="470,222 470,236 560,236 560,226" stroke="var(--green)"/>
      <line x1="595" y1="186" x2="595" y2="208" stroke="var(--green)"/>
    </g>
    <polygon points="230,438 246,424 620,424 620,438" fill="var(--dark)"/>
  </svg>

  <div class="abs section-bar">Director Penalty Notices (DPN)</div>
  <p class="abs back-intro">The ATO uses DPNs and Garnishee Notices to recovery tax obligations on Directors to deal with outstanding PAYG Withholding and Superannuation Guarantee Charge debts (“Tax Debts”).</p>
  <p class="abs back-lead">The DPN regime makes directors of companies who fail to pay liable. The key facts of DPN regime are outlined below</p>

  <div class="abs facts">
    <div class="facts__head">KEY FACTS OF A DIRECTORS PENALTY NOTICE</div>
    <div class="facts__row">
      <div class="facts__label">Director personal liabilities</div>
      <div class="facts__text">Directors become personally liable for Tax Debts 21 days are the DPN Notice is issued</div>
    </div>
    <div class="facts__row">
      <div class="facts__label">Automatic liability for unreported and unpaid Tax Debts</div>
      <div class="facts__text">Where a company’s Tax Debts were both unreported and unpaid 3 months after the due date, the directors are automatically personally liable for the Tax Debts.</div>
    </div>
    <div class="facts__row facts__row--tall">
      <div class="facts__label">Avoiding personal liability for directors once they receive a DPN</div>
      <div class="facts__text">Within 21 days of issuing the DPN (which may be received a week or more after issue), a director can avoid personal liability by either:
        <div class="facts__options"><span>Paying the Tax Debt</span><span>Appointing an Administrator to the company</span><span>Appointing a Liquidator to the company.</span></div>
      </div>
    </div>
    <div class="facts__row">
      <div class="facts__label">Effect on new directors</div>
      <div class="facts__text">New directors are liable if outstanding Tax Debts are unpaid 30 days after their appointment as director</div>
    </div>
    <div class="facts__row">
      <div class="facts__label">Time frames</div>
      <div class="facts__text">ATO can only enforce a DPN after 21 days of giving notice to the director and notice can be given to the company tax agent</div>
    </div>
  </div>

  <div class="abs tips-bar">Tips for directors to limit or avoid personal liability:</div>
  <div class="abs tips">
    <p>Always lodge BAS and SGC Statements within 3 months of the due date, even if the liability cannot be paid!<span class="gap">Seek professional advice from an insolvency practitioner about the options available and possibly save the company through a financial restructure.</span></p>
    <p>Act immediately upon receipt of a DPN and consider a payment arrangement with the ATO. This should be considered with care as payments made can be considered as preference payments to the ATO, if a liquidator is appointed. The ATO can make the directors personally liable for the ATO preference claim</p>
  </div>

  <div class="node" style="left:456px;top:28px;width:72px;height:68px">Business Activity Statement and Superannuation Guarantee Charge lodged within 3 months from due date</div>
  <div class="node" style="left:542px;top:128px;width:60px;height:44px">Director Automatically personally liable</div>
  <div class="node node--bold" style="left:440px;top:158px;width:60px;height:48px">Director not personally liable yet. (Have options) [RIGHTS PRESERVED]</div>
  <span class="tagpill" style="left:438px;top:122px">no</span>
  <span class="tagpill" style="left:545px;top:108px">yes</span>
  <span class="tagpill" style="left:587px;top:196px">yes</span>
  <span class="tagpill" style="left:505px;top:230px">no</span>
  <div class="flow-note" style="left:528px;top:212px;width:56px">Director not personally liable but the company is still insolvent.</div>
  <div class="flow-note" style="left:430px;top:250px;width:120px"><b>If Directors act within 21 days and:</b><br>Wind up Company voluntarily; or<br>Appoint Voluntary Administrator;<br>or<br>Pay debt in full</div>

  <div class="abs web back-web">www.northfieldadvisory.com.au</div>
</section>

</body>
</html>
```